ZRD Roofing Billboard Design

Looking for a fresh new billboard design with my new headshot photo and using some info from my previous billboard and maybe website for design/content inspiration. My website is https://zrdroofing.com/

Also attached are my logo and current lawn sign design. I am looking for something simple, clean and modern. The landing page website should be 3816tops.com like my previous billboard has.

```html
<!DOCTYPE html>
<html lang="en">
<head>
<meta charset="utf-8">
<title>ZRD Roofing Billboard</title>
<link rel="stylesheet" href="https://fonts.googleapis.com/css2?family=Poppins:wght@500;600;700;800&family=Oswald:wght@600&display=swap">
<style>
  :root {
    --canvas: #7b7b7b;
    --navy: #1f3350;
    --navy-deep: #162640;
    --lime: #9db63b;
    --ink: #262626;
    --blue: #1d6a93;
    --red: #e8141b;
    --white: #ffffff;
  }
  * { box-sizing: border-box; margin: 0; padding: 0; }
  html, body {
    width: 1032px;
    height: 1200px;
    overflow: hidden;
    background: var(--canvas);
  }
  .billboard {
    position: absolute;
    left: 26px;
    top: 456px;
    width: 980px;
    height: 287px;
    background: var(--white);
    box-shadow: 0 4px 14px rgba(0,0,0,0.35);
    overflow: hidden;
    font-family: "Poppins", sans-serif;
  }
  .billboard__art {
    position: absolute;
    inset: 0;
    width: 980px;
    height: 287px;
  }
  .headline {
    position: absolute;
    left: 449px;
    white-space: nowrap;
    line-height: 1;
  }
  .headline--top {
    top: 18px;
    font-size: 92px;
    font-weight: 700;
    color: var(--lime);
    letter-spacing: -2px;
  }
  .headline--bottom {
    top: 100px;
    font-size: 55px;
    font-weight: 800;
    color: var(--ink);
    letter-spacing: -1.5px;
  }
  .brand {
    position: absolute;
    left: 418px;
    top: 186px;
    width: 156px;
    display: flex;
    align-items: center;
    gap: 8px;
    font-size: 19px;
    font-weight: 600;
    color: var(--blue);
    white-space: nowrap;
  }
  .brand__dot {
    width: 34px;
    height: 34px;
    border-radius: 50%;
    background: var(--lime);
    flex: none;
  }
  .offer {
    position: absolute;
    left: 589px;
    top: 163px;
    display: flex;
    align-items: center;
  }
  .offer__label {
    height: 42px;
    width: 191px;
    background: var(--blue);
    border-radius: 6px 0 0 6px;
    color: var(--white);
    font-size: 25px;
    font-weight: 500;
    line-height: 42px;
    padding-left: 15px;
    white-space: nowrap;
  }
  .offer__price {
    font-family: "Oswald", sans-serif;
    font-weight: 600;
    font-size: 66px;
    line-height: 1;
    color: var(--red);
    margin-left: -4px;
    margin-top: -8px;
    letter-spacing: -1px;
  }
  .web {
    position: absolute;
    left: 604px;
    top: 226px;
    font-size: 40px;
    font-weight: 700;
    line-height: 1;
    letter-spacing: -1px;
    color: var(--ink);
    white-space: nowrap;
  }
  .web__name { color: var(--blue); }
</style>
</head>
<body>
  <section class="billboard">
    <svg class="billboard__art" viewBox="0 0 980 287" xmlns="http://www.w3.org/2000/svg">
      <defs>
        <linearGradient id="photoTone" x1="0" y1="0" x2="1" y2="1">
          <stop offset="0" stop-color="#2a4262"/>
          <stop offset="1" stop-color="#172a45"/>
        </linearGradient>
      </defs>
      <polygon points="0,0 415,0 312,287 0,287" fill="url(#photoTone)" role="img" aria-label="Headshot of the roofer in a light blue shirt over an aerial view of house rooftops"/>
      <polygon points="415,0 432,0 329,287 312,287" fill="var(--lime)"/>
    </svg>

    <div class="headline headline--top">FULL ROOF</div>
    <div class="headline headline--bottom">REPLACEMENTS</div>

    <div class="brand">
      <span class="brand__dot"></span>
      <span class="brand__name">ZRD Roofing</span>
    </div>

    <div class="offer">
      <div class="offer__label">Starting at</div>
      <div class="offer__price">$7,499</div>
    </div>

    <div class="web"><span class="web__name">3816TOPS</span>.COM</div>
  </section>
</body>
</html>
```